School Fairs flyer design

We are running school fairs (Northfield Residential Academies Expo in East Africa) in February 2018. The school fairs and information sessions will take place in Rwanda (February 6th-8th, Kenya February 9th-10th and Uganda on February 11th-12th.)

Rwanda:
Kigali School Fair: February 7th, 1:30-5:30PM
Student Interviews: February 8th, 9:00-1PM
Location: Kigali Lumora Hotel

For information:
Phone number: +250736482915
Email: info@tovaradvisors.example
www.tovarlearningadvisors.example

Features:
*6 US Boarding Schools representative
*Learn about the application process and apply in person.
* Bring your transcripts/school reports to Interview
* www.tovarlearningadvisors.example

Target Market(s)

Students age 11-20 and their parents

Industry/Entity Type

Education

Contact Information for Business Card

Marcel Habarugira
Executive Director
Tovar Consultants
Dallas, Texas
Marcel@tovaradvisers.example
www.tovaradvisors.example
+1614-527-3186

Number of Pages Required

4 page

Font styles to use
Serif

Colors

Designer to choose colors to be used in the design.

Requirements
Must have
• Very clean, elegant and professional designs. Since we offer educational services to students and families, school tours and fairs, as well as institutional support. We would like the designs to reflect what we do.
Nice to have
• Global view, a new logo that incorporates things from our existing logo. We will use this more often but the targeted population is the same.
Should not have
• off colors

```html
<!DOCTYPE html>
<html lang="en">
<head>
<meta charset="utf-8">
<title>Northfield Residential Academies Expo – East Africa 2018</title>
<link href="https://fonts.googleapis.com/css2?family=Source+Sans+3:wght@400;600;700&display=swap" rel="stylesheet">
<style>
  :root {
    --page-bg: #ece9e4;
    --sun-yellow: #f9bd1f;
    --fair-orange: #e8873a;
    --cream: #fde9b4;
    --ink-brown: #5b4332;
    --ink-grey: #4d4d4d;
    --white: #ffffff;
    --rw-blue: #20a0dc;
    --rw-yellow: #f5d20e;
    --rw-green: #21794a;
    --ke-black: #111111;
    --ke-red: #b8202a;
    --ke-green: #1b7a3c;
    --ug-black: #111111;
    --ug-yellow: #f7d116;
    --ug-red: #d72c2c;
  }
  * { box-sizing: border-box; margin: 0; padding: 0; }
  html, body { width: 900px; height: 1200px; overflow: hidden; }
  body {
    background: var(--page-bg);
    font-family: "Source Sans 3", "Helvetica Neue", Arial, sans-serif;
    position: relative;
  }
  .flyer {
    position: absolute;
    left: 56px; top: 91px;
    width: 788px; height: 1018px;
    overflow: hidden;
    background: linear-gradient(to bottom, var(--white) 0, var(--white) 580px, #fff4d6 760px, var(--cream) 1018px);
  }
  .top-band {
    position: absolute; left: 0; top: 0; width: 100%; height: 280px;
    background: var(--sun-yellow);
  }
  .globe-mark {
    position: absolute; left: 515px; top: 10px;
    width: 200px; height: 200px; border-radius: 50%;
    background: rgba(255,255,255,0.85);
  }
  .headline {
    position: absolute; left: 70px; top: 36px;
    color: var(--white);
    font-weight: 700; font-size: 23px; line-height: 29px;
  }
  .photo-frame {
    position: absolute; left: 58px; top: 104px;
    width: 670px; height: 356px;
    background: var(--white);
  }
  .photo-strip {
    position: absolute; left: 12px; top: 11px;
    width: 646px; height: 345px;
    display: flex; gap: 2px; overflow: hidden;
    background: var(--white);
  }
  .portrait { flex: 1; height: 100%; }
  .portrait-1 { background: linear-gradient(#c9c5c0, #6b4a35 60%, #e8b54a); }
  .portrait-2 { background: linear-gradient(#d6d3cf, #d9b08f 55%, #e2e0dc); }
  .portrait-3 { background: linear-gradient(#cfcac4, #c79a7c 55%, #a9a6a3); }
  .portrait-4 { background: linear-gradient(#cac6c1, #b88266 55%, #8a6752); }
  .portrait-5 { background: linear-gradient(#d1cdc8, #a56e50 55%, #f0f0f0); }
  .portrait-6 { background: linear-gradient(#d8d5d0, #d9ae92 55%, #f1e3a2); }
  .brand-badge {
    position: absolute; left: 252px; top: 250px;
    width: 170px; height: 170px; border-radius: 50%;
    background: var(--white);
    display: flex; align-items: flex-start; justify-content: center;
    padding-top: 44px;
  }
  .brand-name {
    color: var(--ke-black);
    font-weight: 700; font-size: 17px; line-height: 20px;
    text-align: center; width: 120px;
  }
  .event-title {
    position: absolute; left: 0; top: 503px; width: 100%;
    text-align: center;
    color: var(--fair-orange);
    font-weight: 700; font-size: 28px; line-height: 36px;
  }
  .world-watermark {
    position: absolute; left: 220px; top: 565px;
    width: 340px; height: 340px; border-radius: 50%;
    background: rgba(250, 214, 160, 0.35);
  }
  .orange-band {
    position: absolute; left: 0; top: 700px; width: 100%; height: 70px;
    background: var(--fair-orange);
  }
  .tilted {
    position: absolute;
    transform: translate(-50%, -50%) rotate(-28deg);
    white-space: nowrap;
    color: var(--ink-brown);
    font-weight: 700; font-size: 21px;
  }
  .flag-card {
    position: absolute;
    width: 212px; height: 136px;
    transform: translate(-50%, -50%) rotate(-28deg);
    background: var(--white);
    padding: 6px;
    box-shadow: 2px 4px 8px rgba(0,0,0,0.3);
  }
  .flag-card svg { display: block; width: 100%; height: 100%; }
  .services {
    position: absolute; left: 0; top: 916px; width: 100%;
    text-align: center;
    color: var(--ink-grey);
    font-size: 16px; line-height: 21px;
  }
  .services span { margin: 0 6px; }
</style>
</head>
<body>
  <main class="flyer">
    <div class="top-band"></div>
    <div class="globe-mark" role="img" aria-label="Light globe grid decoration"></div>
    <h2 class="headline">Schedule Your Child's Interviews<br>with the Boarding Schools</h2>

    <div class="photo-frame">
      <div class="photo-strip">
        <div class="portrait portrait-1" role="img" aria-label="Portrait of a smiling student"></div>
        <div class="portrait portrait-2" role="img" aria-label="Portrait of a smiling student"></div>
        <div class="portrait portrait-3" role="img" aria-label="Portrait of a smiling student"></div>
        <div class="portrait portrait-4" role="img" aria-label="Portrait of a smiling student"></div>
        <div class="portrait portrait-5" role="img" aria-label="Portrait of a smiling student"></div>
        <div class="portrait portrait-6" role="img" aria-label="Portrait of a smiling student with glasses"></div>
        <div class="brand-badge"><span class="brand-name">Tovar Consultants</span></div>
      </div>
    </div>

    <h1 class="event-title">Northfield Residential Academies Expo<br>East Africa 2018</h1>

    <div class="world-watermark" role="img" aria-label="Faint globe decoration"></div>
    <div class="orange-band"></div>

    <span class="tilted" style="left:158px; top:638px;">Rwanda</span>
    <span class="tilted" style="left:395px; top:643px;">Kenya</span>
    <span class="tilted" style="left:630px; top:643px;">Uganda</span>

    <div class="flag-card" style="left:160px; top:733px;">
      <svg viewBox="0 0 200 124" preserveAspectRatio="none" aria-label="Flag of Rwanda">
        <rect width="200" height="62" fill="var(--rw-blue)"/>
        <rect y="62" width="200" height="31" fill="var(--rw-yellow)"/>
        <rect y="93" width="200" height="31" fill="var(--rw-green)"/>
        <circle cx="160" cy="28" r="12" fill="var(--rw-yellow)"/>
      </svg>
    </div>
    <div class="flag-card" style="left:393px; top:735px;">
      <svg viewBox="0 0 200 124" preserveAspectRatio="none" aria-label="Flag of Kenya">
        <rect width="200" height="124" fill="var(--white)"/>
        <rect width="200" height="37" fill="var(--ke-black)"/>
        <rect y="44" width="200" height="36" fill="var(--ke-red)"/>
        <rect y="87" width="200" height="37" fill="var(--ke-green)"/>
        <ellipse cx="100" cy="62" rx="18" ry="38" fill="var(--ke-red)"/>
      </svg>
    </div>
    <div class="flag-card" style="left:627px; top:733px;">
      <svg viewBox="0 0 200 124" preserveAspectRatio="none" aria-label="Flag of Uganda">
        <rect y="0" width="200" height="21" fill="var(--ug-black)"/>
        <rect y="21" width="200" height="21" fill="var(--ug-yellow)"/>
        <rect y="42" width="200" height="20" fill="var(--ug-red)"/>
        <rect y="62" width="200" height="21" fill="var(--ug-black)"/>
        <rect y="83" width="200" height="20" fill="var(--ug-yellow)"/>
        <rect y="103" width="200" height="21" fill="var(--ug-red)"/>
        <circle cx="100" cy="62" r="20" fill="var(--white)"/>
      </svg>
    </div>

    <span class="tilted" style="left:168px; top:826px;">February 6th-8th</span>
    <span class="tilted" style="left:402px; top:830px;">February 9th-10th</span>
    <span class="tilted" style="left:636px; top:826px;">February 11th-12th</span>

    <p class="services">
      <span>•</span>Educational Services to Students and Families<span>•</span>School Tours and Fairs<span>•</span><br>
      <span>•</span>Institutional Support<span>•</span>
    </p>
  </main>
</body>
</html>
```